Play Equipment Distributor Website

We need a design (no coding) of a website for our play equipment sales company. The website will be in Japanese and is targeted at the Japanese market, and as such should be designed with that in mind.
The website will have 5 sections: home/top, products, safety, company information, contact. Initially we would like to have the top and Pebble Climb Works (our main product) pages designed. The main call to action - Request Catalog - should be present on all pages. The copy is still in the making, so please use Japanese dummy text to fill the pages for now.
For inspiration regarding the design, this is a website that we like very much: http://www.yardloopgear.example/
Attaching our logo, other graphics, as well as a rough idea of what we have on our mind in terms of layout and content of each page.
Target Market(s)
Japanese playset users - kindergartens, schools, entertainment parks, etc.

```html
<!DOCTYPE html>
<html lang="ja">
<head>
<meta charset="utf-8">
<title>Kiboh Play Japan</title>
<link href="https://fonts.googleapis.com/css2?family=Oswald:wght@300;400;500&family=Raleway:wght@400;600&family=Noto+Sans+JP:wght@400;700&display=swap" rel="stylesheet">
<style>
:root{
  --green:#3f8f2c;
  --green-dark:#2e7a1f;
  --lime:#7dc142;
  --grey:#ececec;
  --line:#9cc98a;
  --ink:#333;
}
*{margin:0;padding:0;box-sizing:border-box}
html,body{width:1200px;height:1120px;overflow:hidden;background:#fff}
.page{position:absolute;left:450px;top:0;width:298px;height:1120px;background:#fff;font-family:"Noto Sans JP",sans-serif;color:var(--ink)}
.abs{position:absolute}
.hero{left:0;top:0;width:298px;height:222px;background:var(--grey)}
.brand{left:18px;top:12px;display:flex;align-items:center;gap:4px;font-family:"Raleway",sans-serif;font-weight:600;font-size:8px;line-height:8px;color:var(--green-dark)}
.brand i{display:block;width:8px;height:8px;background:var(--green)}
.nav{left:128px;top:0;display:flex}
.nav a{display:block;width:32px;height:38px;font-size:3.4px;color:#999;text-decoration:none;text-align:center;padding-top:28px}
.nav a.active{background:var(--green);color:#fff;width:26px;margin-right:6px}
.hero-title{left:0;width:298px;top:60px;text-align:center;font-weight:700;font-size:4.4px;line-height:6px;color:var(--green-dark)}
.hero-copy{left:50px;width:198px;top:82px;text-align:center;font-size:3.6px;line-height:6px}
.photo{display:block}
.hero-photo{left:18px;top:104px;width:264px;height:108px;background:radial-gradient(ellipse at 50% 55%,#b9794a 0%,#c99a6c 40%,rgba(236,236,236,0) 70%)}
.banner{left:0;width:298px;height:87px;background:linear-gradient(120deg,#3c8a2a,#4b9a32 60%,#3a8428)}
.banner p{position:absolute;left:0;width:298px;top:38px;text-align:center;color:#fff;font-family:"Raleway",sans-serif;font-size:7.4px;line-height:12px}
.btn{position:absolute;background:#fff;color:var(--green-dark);font-family:"Oswald",sans-serif;font-size:4px;letter-spacing:.8px;text-align:center}
.banner .btn{left:122px;top:63px;width:53px;height:11px;line-height:11px}
.heading{left:21px;width:256px;height:14px;display:flex;align-items:center;gap:6px}
.heading::before,.heading::after{content:"";flex:1;height:.6px;background:var(--line)}
.heading h2{font-family:"Oswald",sans-serif;font-weight:400;font-size:11px;line-height:14px;color:#222;white-space:nowrap}
.heading h2 span{color:var(--lime)}
.heading.spaced h2{letter-spacing:2.4px;font-weight:300;font-size:10px}
.heading small{position:absolute;left:0;right:0;top:15px;text-align:center;font-size:3.6px;color:var(--lime)}
.body{font-size:3.5px;line-height:6.6px}
.thumb{width:58px;height:36px}
.tt{font-family:"Oswald",sans-serif;font-size:5px;color:var(--lime)}
.tile{border:2px solid #e4e4e4}
.circle{position:absolute;border-radius:50%;background:rgba(125,193,66,.92);color:#fff;font-family:"Oswald",sans-serif;font-size:6px;line-height:7px;text-align:center;display:flex;align-items:center;justify-content:center}
.tag{position:absolute;right:0;bottom:3px;background:rgba(125,193,66,.95);color:#fff;font-family:"Oswald",sans-serif;font-size:5px;padding:2px 4px}
.contact{left:0;top:960px;width:298px;height:160px;background:var(--grey)}
.info{font-size:3.8px;line-height:5px;display:flex;gap:4px}
.foot-line{left:21px;width:256px;top:142px;height:.6px;background:var(--line)}
.copy{left:0;width:298px;top:149px;text-align:center;font-size:3px;letter-spacing:.6px;color:#777;font-family:"Raleway",sans-serif}
</style>
</head>
<body>
<div class="page">

  <section class="abs hero">
    <div class="abs brand"><i></i>KIBOH PLAY<br>JAPAN</div>
    <nav class="abs nav">
      <a class="active" href="#">トップ</a><a href="#">製品</a><a href="#">安全</a><a href="#">会社</a><a href="#">連絡</a>
    </nav>
    <div class="abs hero-title">子どもたちの遊びを広げる<br>安全で楽しい遊具をお届けします</div>
    <div class="abs hero-copy">幼稚園や学校、公園のための木製遊具を日本全国にお届けしています。安全性と耐久性にこだわった製品で、子どもたちの笑顔を支えます。</div>
    <div class="abs photo hero-photo" role="img" aria-label="Wooden playset with yellow slides and children playing"></div>
  </section>

  <section class="abs banner" style="top:222px" role="img" aria-label="Green tinted photo of a child on a playground">
    <p>Solving the play Deficit by Providing<br>Fun and affordable Play Equipment!</p>
    <a class="btn">REQUEST CATALOG</a>
  </section>

  <div class="abs heading spaced" style="top:321px"><h2>IMPORTANCE <span>OF PLAY</span></h2><small>遊びの大切さについて</small></div>
  <div class="abs photo" style="left:25px;top:351px;width:111px;height:71px;background:linear-gradient(135deg,#f3d21a 0%,#e9c94a 35%,#cfb08a 60%,#9b5e33 100%)" role="img" aria-label="Girl sitting inside a yellow slide"></div>
  <div class="abs body" style="left:146px;top:366px;width:126px">遊びは子どもの心と体の成長に欠かせないものです。外で体を動かし、友だちと関わることで、社会性や創造力、判断力が自然に育まれます。私たちは安心して遊べる環境づくりを通して、子どもたちの健やかな毎日を応援します。</div>

  <div class="abs heading" style="top:440px"><h2>PLAY <span>DEFICIT</span></h2><small>遊び不足の現状について</small></div>
  <div class="abs body" style="left:27px;top:481px;width:126px">近年、子どもたちが外で遊ぶ時間は大きく減っています。安全な遊び場の不足や生活習慣の変化により、体力や運動能力の低下が指摘されています。私たちは楽しく手頃な遊具でこの課題に取り組みます。</div>
  <div class="abs photo" style="left:160px;top:469px;width:110px;height:69px;background:linear-gradient(160deg,#c9b8a4,#8f5a34 45%,#3f6b3a 100%)" role="img" aria-label="Playset with yellow tube slide on green turf"></div>

  <div class="abs photo thumb" style="left:27px;top:545px;background:linear-gradient(135deg,#8b5a36,#c98f56)" role="img" aria-label="Child at playset window"></div>
  <div class="abs photo thumb" style="left:88px;top:545px;background:radial-gradient(circle at 50% 50%,#e8c23a 0 30%,#8a5a34 60%)" role="img" aria-label="Child looking through steering wheel"></div>
  <div class="abs photo thumb" style="left:151px;top:545px;background:linear-gradient(135deg,#2f5a2a,#c9356a 60%,#7a3b3b)" role="img" aria-label="Child in pink crawl tube"></div>
  <div class="abs photo thumb" style="left:212px;top:545px;background:linear-gradient(135deg,#f0d23a,#b07842 60%,#5d8a3a)" role="img" aria-label="Boy with yellow slide"></div>

  <div class="abs" style="left:27px;top:585px;width:56px"><div class="tt">YOUR TITLE</div><div class="body" style="line-height:6px">楽しい遊びで体を育てる工夫を紹介します。</div></div>
  <div class="abs" style="left:88px;top:585px;width:56px"><div class="tt">YOUR TITLE</div><div class="body" style="line-height:6px">楽しい遊びで体を育てる工夫を紹介します。</div></div>
  <div class="abs" style="left:151px;top:585px;width:56px"><div class="tt">YOUR TITLE</div><div class="body" style="line-height:6px">楽しい遊びで体を育てる工夫を紹介します。</div></div>
  <div class="abs" style="left:212px;top:585px;width:56px"><div class="tt">YOUR TITLE</div><div class="body" style="line-height:6px">楽しい遊びで体を育てる工夫を紹介します。</div></div>

  <section class="abs banner" style="top:628px" role="img" aria-label="Green tinted photo of a child on a playground">
    <p>Solving the play Deficit by Providing<br>Fun and affordable Play Equipment!</p>
    <a class="btn">REQUEST CATALOG</a>
  </section>

  <div class="abs heading" style="top:729px"><h2>OUR <span>PRODUCTS</span></h2><small>製品ラインナップのご紹介</small></div>

  <div class="abs photo tile" style="left:25px;top:759px;width:147px;height:92px;background:linear-gradient(180deg,#6d9a5a,#9b6a3c 50%,#c8a870)" role="img" aria-label="Children gathered around a large playset"><div class="circle" style="left:48px;top:20px;width:52px;height:52px">PEBBLE<br>PLAYSETS</div></div>
  <div class="abs photo tile" style="left:25px;top:858px;width:147px;height:92px;background:linear-gradient(180deg,#d8d8d0,#8d5b35 55%,#4a3a30)" role="img" aria-label="Crowd of children at a play event"><div class="circle" style="left:48px;top:20px;width:52px;height:52px">PLAY<br>EVENTS</div></div>
  <div class="abs photo tile" style="left:178px;top:759px;width:95px;height:59px;background:linear-gradient(180deg,#3f7a34,#6aa048 60%,#b07a4a)" role="img" aria-label="Children on spring rockers"><span class="tag">SPRING ROCKERS</span></div>
  <div class="abs photo tile" style="left:178px;top:825px;width:95px;height:59px;background:linear-gradient(135deg,#8b5a34,#e5c53a 55%,#6a8a3a)" role="img" aria-label="Multi court playset"><span class="tag">MULTI COURT</span></div>
  <div class="abs photo tile" style="left:178px;top:890px;width:95px;height:60px;background:linear-gradient(160deg,#b8b0a4,#8a5634 50%,#3f6e34)" role="img" aria-label="Playset on artificial turf"><span class="tag">ARTIFICIAL TURF</span></div>

  <section class="abs contact">
    <div class="abs heading" style="top:37px"><h2>CONTACT <span>US</span></h2></div>
    <div class="abs" style="left:39px;top:70px;width:86px">
      <div class="info"><svg width="6" height="6" viewBox="0 0 10 10"><path d="M5 1a3 3 0 0 1 3 3c0 2-3 5-3 5S2 6 2 4a3 3 0 0 1 3-3z" fill="none" stroke="#3f8f2c" stroke-width="1.2"/></svg><span>東京都港区桜ヶ丘町1-2-3<br>さくらビル5階</span></div>
      <div class="info" style="margin-top:6px"><svg width="6" height="6" viewBox="0 0 10 10"><rect x="1" y="2.5" width="8" height="5" fill="#3f8f2c"/></svg><span>info@kibohplay.example</span></div>
      <div class="info" style="margin-top:6px"><svg width="6" height="6" viewBox="0 0 10 10"><path d="M2 1l2 2-1 1.5c1 1.5 2 2.5 3.5 3.5L8 6l2 2-1.5 1.5C5 9 1 5 .5 1.5z" fill="#3f8f2c"/></svg><span>+1.305-555-0142</span></div>
      <a class="btn" style="left:0;top:44px;width:54px;height:11px;line-height:11px;background:var(--green);color:#fff;border:1px solid #fff;outline:.6px solid var(--green)">REQUEST CATALOG</a>
    </div>
    <div class="abs photo" style="left:121px;top:62px;width:139px;height:71px;background:linear-gradient(135deg,#e4e4e0,#d5d8d2 50%,#e9e2c4)" role="img" aria-label="Street map showing office location"></div>
    <div class="abs foot-line"></div>
    <div class="abs copy">COPYRIGHT © 2016. KIBOH PLAY JAPAN . ALL RIGHTS RESERVED</div>
  </section>

</div>
</body>
</html>
```